International Student Travel Company needs a web page re-designed

Halvard Tours is a worldwide leader in student educational and performing arts travel programs. We provide high-quality tours that exceed the expectations of our participants/customers and enhance a student's learning experiences. Our mission is to forever change how every student sees the world around them. Our company has 3 distinct brands: Halvard Tours (www.halvardtours.example), Meridale Tours (www.meridaletours.example) and Pellwood Legacy Tours & Music Galas (www.pellgala.example).

As part of our travel programs, we offer participants the option to purchase travel insurance. We are looking to re-design the page that offers each participant the option to buy insurance during their online registration process to maximize the number of customers who purchase the recommended option. The registration process is set up behind a password protected registration website.

Here is a link to view the current page for each brand:
https://accounts.halvardtours.example/tech/demo/8656
https://accounts.meridaletours.example/tech/demo/8656
https://accounts.pellgala.example/tech/demo/8656

We are attaching the HTML for the current page so you can start with the current format that this design is a part of- for example, the header & footer and the "Registration Step # section".

Please note that this current design was created for the "Meridale Tours" brand as you may note the use of the orange color on the page. We would like to design the page so that we can easily implement the same design for all 3 brands. As you will see from looking at the brands online, they all share a similar blue that can be used where we need a color as you will see on our SAMPLE mock-up that we have included as an attachment.

In our SAMPLE mock-up (file attached named "SAMPLE webpage mock-up.pdf") we have icons at the top of the insurance option which is meant to be a link to a PDF that is an advertisement for each type of travel insurance. So, however you decide to design that element, please make sure to include that as a link that will open a PDF in a new tab. The "None" option will open up the PDF attached named "Note to Parents.pdf". The "Scholar Prime" option will open up the PDF attached named "Odette & Marla.pdf". The "Scholar Prime with CFAR" option will open up the PDF attached named "CFAR.pdf".

The sample mock-up is just a sample draft idea of how we would want it to look. Please feel free to re-design completely or as close to this design as you wish using your best design judgment. The goal is to make it look very professional and convince customers to select the recommended "Scholar Prime with CFAR" option as this will fully protect them in case they need to cancel.

It is very important to use all the copy as its presented since the language has all been approved by the insurance company's compliance team.

*VERY IMPORTANT*
Please design this so that it is MOBILE friendly. Many of our customers register for our trips on their mobile devices. So, because we are presenting 3 options to compare we need to make sure the design works well on small mobile screens. So, please present your designs for both large computer screens and small mobile devices so we can see how it would look at the various different screen sizes.

Please let us know if you have any questions or require any more info from us to get started. We are looking forward to seeing your designs!

-Halvard Tours Marketing Team

```html
<!DOCTYPE html>
<html lang="en">
<head>
<meta charset="utf-8">
<title>Halvard Tours – Travel Payment Protection</title>
<link rel="stylesheet" href="https://fonts.googleapis.com/css2?family=Merriweather:wght@700;900&family=Roboto:wght@400;500;700&display=swap">
<style>
:root{
  --navy:#0b2c93;
  --navy-deep:#08247a;
  --orange:#e2661c;
  --page:#f0f2fb;
  --white:#ffffff;
  --ink:#1b1b1b;
  --muted:#6d6f78;
  --line:#e3e5ee;
  --frame:#d7dae8;
  --green:#3d8a1f;
  --red:#d11f2b;
  --stage:#6f6f6f;
}
*{box-sizing:border-box;margin:0;padding:0}
html,body{width:1200px;height:3940px;overflow:hidden}
body{background:var(--stage);font-family:"Roboto",Arial,sans-serif;color:var(--ink);position:relative}
.screen{position:absolute;background:var(--page);overflow:hidden}
.screen--desktop{left:73px;top:73px;width:812px;height:1864px}
.screen--mobile{left:923px;top:73px;width:204px;height:3792px}
.abs{position:absolute}

/* header */
.site-header{position:absolute;left:0;top:0;width:100%;background:var(--white);border-top:3px solid var(--navy)}
.brand{position:absolute;display:flex;align-items:center;gap:6px;font-family:"Merriweather",Georgia,serif;font-weight:700;color:var(--red)}
.brand__dot{border-radius:50%;background:var(--red)}
.nav{position:absolute;display:flex;gap:16px;font-size:7.5px;font-weight:700;color:#222}
.nav a{color:inherit;text-decoration:none;padding-bottom:3px}
.nav .is-active{border-bottom:2px solid var(--orange)}
.btn{display:flex;align-items:center;justify-content:center;background:var(--orange);color:var(--white);font-weight:700;border-radius:20px;text-transform:uppercase;text-decoration:none}
.burger{position:absolute;width:11px;height:9px;border-top:2px solid #222;border-bottom:2px solid #222}
.burger::after{content:"";position:absolute;left:0;right:0;top:1.5px;border-top:2px solid #222}

/* hero */
.hero-photo{position:absolute;left:0;width:100%;background:linear-gradient(180deg,#1f5fc7 0%,#3d86e0 45%,#8cbcee 100%)}
.hero-band{position:absolute;left:0;width:100%;background:var(--navy);color:var(--white)}
.hero-title{font-family:"Merriweather",Georgia,serif;font-weight:700;line-height:1.1}
.hero-text{line-height:1.75}

.section-title{font-family:"Merriweather",Georgia,serif;font-weight:700;color:#151515;text-align:center}
.intro{color:var(--muted);text-align:center}
.partner{position:absolute;display:flex;align-items:center;gap:6px;background:var(--white);color:var(--navy);font-weight:700}
.partner__square{background:var(--navy)}

.cost-box{position:absolute;background:var(--white);border:1px solid var(--frame);display:flex;align-items:center;justify-content:center;font-weight:500}
.cost-box b,.cost-line b{color:var(--orange);font-weight:500}

.recommended{position:absolute;color:var(--orange);font-size:6.5px;text-align:center}

/* plan cards */
.plan{position:absolute;background:var(--white);display:flex;flex-direction:column;box-shadow:0 1px 4px rgba(20,30,80,.12)}
.plan__head{position:relative;height:70px;background:var(--navy);color:var(--white);text-align:center;font-weight:700;font-size:13.5px;padding-top:16px;line-height:1.05}
.plan--featured .plan__head{background:var(--orange);height:80px;font-size:14px;padding-top:14px}
.plan__info{position:absolute;right:5px;top:4px;width:8px;height:8px;border-radius:50%;background:var(--white);color:var(--navy);font-size:6px;line-height:8px;font-weight:700}
.plan--featured .plan__info{color:var(--orange)}
.plan__price{position:absolute;left:50%;bottom:-25px;transform:translateX(-50%);width:50px;height:50px;border-radius:50%;background:var(--white);border:3px solid var(--navy);color:var(--navy);display:flex;align-items:center;justify-content:center;font-size:14px;font-weight:700}
.plan--featured .plan__price{width:62px;height:62px;bottom:-31px;border-color:var(--orange);color:var(--orange);font-size:15px}
.plan__lead{margin:36px 18px 10px;text-align:center;font-size:9px;font-weight:500;line-height:1.3}
.plan--featured .plan__lead{margin-top:44px}
.plan__list{list-style:none;margin:0 12px 0 14px;font-size:7px;color:var(--muted);line-height:1.35}
.plan__list li{position:relative;padding-left:15px;margin-bottom:9px}
.plan__list li::before{content:"";position:absolute;left:2px;top:0;width:3px;height:6px;border-right:1.5px solid var(--navy);border-bottom:1.5px solid var(--navy);transform:rotate(45deg)}
.plan--featured .plan__list li::before{border-color:var(--orange)}
.plan__list li.is-plus{color:var(--green)}
.plan__list li.is-plus::before{border-color:var(--green)}
.plan__list li.is-no{color:var(--red)}
.plan__list li.is-no::before{content:"✖";border:0;transform:none;width:auto;height:auto;top:0;left:1px;font-size:7px;color:var(--red)}
.plan__foot{margin-top:auto;border-top:1px dashed var(--line);padding:8px 0 9px;display:flex;justify-content:center}
.plan__select{width:64px;height:16px;font-size:7px}

.feedback-tab{position:absolute;background:var(--orange);border-radius:16px;color:var(--white);font-weight:700;display:flex;align-items:center;justify-content:center}
.feedback-tab span{writing-mode:vertical-rl;transform:rotate(180deg);white-space:nowrap}

/* benefit columns */
.bcol{position:absolute;background:var(--white);border:1px solid var(--frame);font-size:6.6px;color:#333}
.bcol__row{height:30px;margin:0 9px;display:flex;align-items:center;justify-content:center;text-align:center;border-bottom:1px solid var(--line);line-height:1.35}
.bcol__row:last-child{border-bottom:0}
.bcol__row--head{height:36px}
.bcol__row--tall{height:38px}
.bcol__row--cfar{color:var(--green);font-size:6px;text-transform:uppercase}
.bcol__label{width:100%;height:22px;background:var(--navy);color:var(--white);display:flex;align-items:center;justify-content:center;font-size:11px;font-weight:500;letter-spacing:.3px}
.bcol__x{color:var(--red);font-size:7px}
.bcol--m{font-size:5.6px}
.bcol--m .bcol__row{margin:0 6px}
.bcol--m .bcol__row--cfar{font-size:5.2px}
.bcol--m .bcol__label{font-size:10px;height:20px}

.coverage-note{position:absolute;color:var(--navy);font-weight:500;line-height:1.45}
.footnotes{position:absolute;color:#333}
.footnotes p{margin:0}
.footnotes .star{color:var(--red)}
.policy-code{position:absolute;font-weight:700;color:#222}

.site-footer{position:absolute;left:0;width:100%;background:var(--navy);color:var(--white);display:flex;align-items:center;justify-content:center;text-align:center}
</style>
</head>
<body>

<!-- ================= DESKTOP ================= -->
<main class="screen screen--desktop">
  <header class="site-header" style="height:49px">
    <div class="brand" style="left:98px;top:8px;font-size:19px">
      <span class="brand__dot" style="width:26px;height:26px"></span>Halvard Tours
    </div>
    <nav class="nav" style="left:355px;top:18px">
      <a class="is-active" href="#">HOME</a><a href="#">ABOUT US</a><a href="#">PRICING</a><a href="#">CONTACT US</a>
    </nav>
    <a class="btn" href="#" style="position:absolute;left:587px;top:12px;width:126px;height:23px;font-size:5.8px">Travel Protection Options</a>
  </header>

  <div class="hero-photo" style="top:49px;height:295px" role="img" aria-label="Photo of a smiling student traveller holding a map in front of the Eiffel Tower under a blue sky"></div>
  <section class="hero-band" style="top:344px;height:88px">
    <h1 class="hero-title abs" style="left:104px;top:13px;font-size:27px">Travel Payment<br>Protection</h1>
    <p class="hero-text abs" style="left:410px;top:17px;width:305px;font-size:8.3px">Travel Insurance is optional, but unexpected events are always a possibility... and without the Scholar Prime Group Travel Protection, you might lose up to 100% of your trip investment</p>
  </section>

  <h2 class="section-title abs" style="left:0;width:100%;top:478px;font-size:30px">Protect your Trip Investment!</h2>
  <p class="intro abs" style="left:150px;width:512px;top:530px;font-size:8.3px;line-height:17px">Voyagard Assurance, a leading provider of group travel insurance, offers participants the opportunity to protect their travel investment.This program offers an array of travel protection benefits including 24/7 Worldwide Non-Insurance Assistance Services as well as Trip Cancellation,Trip Interruption, Medical Expense, Baggage and Personal Effects, and more travel insurance coverages such as the Cancel for Any Reason (CFAR) option, if eligible</p>
  <div class="partner" style="left:315px;top:623px;width:182px;height:48px;padding:0 10px;font-size:12.5px">
    <span class="partner__square" style="width:30px;height:30px"></span>Voyagard Assurance
  </div>
  <div class="cost-box" style="left:213px;top:705px;width:388px;height:32px;font-size:14.5px">To start, please enter your total Trip Cost:&nbsp;<b>$150</b></div>

  <a class="feedback-tab" href="#" style="left:144px;top:852px;width:32px;height:245px;font-size:12px"><span>QUESTIONS AND COMMENTS?</span></a>

  <div class="recommended" style="left:562px;width:151px;top:786px">★ Recommended ★</div>

  <article class="plan" style="left:231px;top:805px;width:150px;height:341px">
    <div class="plan__head">None<span class="plan__info">?</span><span class="plan__price">$0</span></div>
    <p class="plan__lead">Potentially lose 100% of your tour cost</p>
    <ul class="plan__list"><li>No Payment Protection</li></ul>
    <div class="plan__foot"><a class="btn plan__select" href="#">Select</a></div>
  </article>

  <article class="plan plan--featured" style="left:381px;top:788px;width:181px;height:358px">
    <div class="plan__head">Scholar Prime<span class="plan__info">?</span><span class="plan__price">$100</span></div>
    <p class="plan__lead">Protects your trip investment for covered reasons only</p>
    <ul class="plan__list">
      <li>Trip Cancellation coverage provides a 100% refund if you need to cancel for covered reasons</li>
      <li>Includes additional coverages as per below Schedule</li>
      <li class="is-no">Does NOT include Cancel for Any Reason (CFAR)***</li>
      <li class="is-no">No coverage for cancellations due to fear of a pandemic</li>
    </ul>
    <div class="plan__foot"><a class="btn plan__select" href="#">Select</a></div>
  </article>

  <article class="plan" style="left:562px;top:803px;width:151px;height:343px">
    <div class="plan__head" style="font-size:13px;padding-top:10px">Scholar Prime with<br>CFAR<span class="plan__info">?</span><span class="plan__price">$150</span></div>
    <p class="plan__lead">Potentially lose 100% of your tour cost</p>
    <ul class="plan__list" style="font-size:6.6px">
      <li>Trip Cancellation coverage provides a 100% refund if you need to cancel for covered reasons</li>
      <li>Includes additional coverages as per below Schedule</li>
      <li class="is-plus">Includes Cancel for Any Reason (CFAR)***</li>
      <li class="is-plus">Covers cancellation due to fear of a pandemic ***</li>
    </ul>
    <div class="plan__foot"><a class="btn plan__select" href="#">Select</a></div>
  </article>

  <div class="bcol" style="left:100px;top:1146px;width:150px">
    <div class="bcol__row bcol__row--head"><span class="bcol__label">BENEFIT</span></div>
    <div class="bcol__row bcol__row--cfar">Cancel for any reason (CFAR)***</div>
    <div class="bcol__row">Trip Cancellation**</div>
    <div class="bcol__row">Trip Interruption**</div>
    <div class="bcol__row">Travel Delay – 6 Hours</div>
    <div class="bcol__row">Missed Connection – 3 Hours</div>
    <div class="bcol__row">Baggage/Personal Effects</div>
    <div class="bcol__row">Baggage Delay – 24 Hours</div>
    <div class="bcol__row bcol__row--tall">Emergency Medical Evacuation, Medical Repatriation &amp; Return of Remains</div>
    <div class="bcol__row">Accident &amp; Sickness Medical Expense</div>
    <div class="bcol__row">Non-Medical Emergency Evacuation</div>
    <div class="bcol__row bcol__row--tall">Non-Insurance Worldwide Emergency Assistance Services</div>
  </div>
  <div class="bcol" style="left:250px;top:1146px;width:152px">
    <div class="bcol__row bcol__row--head"></div>
    <div class="bcol__row"><span class="bcol__x">✖</span></div>
    <div class="bcol__row"><span class="bcol__x">✖</span></div>
    <div class="bcol__row"><span class="bcol__x">✖</span></div>
    <div class="bcol__row"><span class="bcol__x">✖</span></div>
    <div class="bcol__row"><span class="bcol__x">✖</span></div>
    <div class="bcol__row"><span class="bcol__x">✖</span></div>
    <div class="bcol__row"><span class="bcol__x">✖</span></div>
    <div class="bcol__row bcol__row--tall"><span class="bcol__x">✖</span></div>
    <div class="bcol__row"><span class="bcol__x">✖</span></div>
    <div class="bcol__row"><span class="bcol__x">✖</span></div>
    <div class="bcol__row bcol__row--tall"><span class="bcol__x">✖</span></div>
  </div>
  <div class="bcol" style="left:402px;top:1146px;width:160px">
    <div class="bcol__row bcol__row--head"></div>
    <div class="bcol__row"><span class="bcol__x">✖</span></div>
    <div class="bcol__row">Trip Cost*</div>
    <div class="bcol__row">150% Trip Cost</div>
    <div class="bcol__row">$750 ($150/day)</div>
    <div class="bcol__row">$500</div>
    <div class="bcol__row">$1,500</div>
    <div class="bcol__row">$300</div>
    <div class="bcol__row bcol__row--tall">$100,000</div>
    <div class="bcol__row">$25,000</div>
    <div class="bcol__row">$100,000</div>
    <div class="bcol__row bcol__row--tall">Included</div>
  </div>
  <div class="bcol" style="left:562px;top:1146px;width:151px">
    <div class="bcol__row bcol__row--head bcol__row--cfar" style="margin-bottom:0">Cancel for any reason (CFAR)***: Included</div>
    <div class="bcol__row">Trip Cost*</div>
    <div class="bcol__row">150% of Trip Cost</div>
    <div class="bcol__row">$750 ($150/day)</div>
    <div class="bcol__row">$500</div>
    <div class="bcol__row">$1,500</div>
    <div class="bcol__row">$300</div>
    <div class="bcol__row bcol__row--tall">$100,000</div>
    <div class="bcol__row">$25,000</div>
    <div class="bcol__row">$100,000</div>
    <div class="bcol__row bcol__row--tall">Included</div>
    <div class="bcol__row" style="height:0;border:0"></div>
  </div>

  <p class="coverage-note" style="left:98px;top:1558px;width:500px;font-size:12px">Coverages may vary and not all coverage is available in all jurisdictions. Totals listed below each coverage are the maximum benefit amount payable.</p>
  <div class="footnotes" style="left:98px;top:1610px;width:590px;font-size:6.8px;line-height:16.5px">
    <p><span class="star">*</span> Up to the lesser of the Trip Cost paid or the limit of Coverage for which benefits are requested and the appropriate plan cost has been paid. Maximum limit of $10,000</p>
    <p><span class="star">**</span> For $0 Trip Cost, there is no Trip Cancellation and Trip Interruption is limited to $500 return air only</p>
    <p><span class="star">***</span> CFAR coverage is the lesser of 75% of the nonrefundable trip cost or up to the maximum of $10,000. CFAR is optional and available for purchase on an individual level. Trip cancellation must be 48 hours or more prior to scheduled departure. CFAR must be purchased at the time of plan purchase and with, or before your final payment. CFAR is available if you paid your Travel Supplier for the full cost for all non-refundable trip costs for your trip prior to your cancellation of your trip. For $0 Trip Cost there is no CFAR. <b>This benefit is not available to residents of New York State.</b></p>
  </div>
  <a class="btn" href="#" style="position:absolute;left:98px;top:1729px;width:224px;height:29px;font-size:7.2px;font-weight:500">Click here for limitations and exclusions</a>
  <span class="policy-code" style="left:333px;top:1738px;font-size:10px">VG-4180</span>

  <footer class="site-footer" style="top:1811px;height:53px;font-size:8px">© 2020 Halvard Tours.All Rights reserved &nbsp;|&nbsp;Privacy Policy &nbsp;|&nbsp; Terms and use</footer>
</main>

<!-- ================= MOBILE ================= -->
<main class="screen screen--mobile">
  <header class="site-header" style="height:46px;background:var(--white)">
    <div class="brand" style="left:5px;top:10px;font-size:9px;gap:3px">
      <span class="brand__dot" style="width:12px;height:12px"></span>Halvard Tours
    </div>
    <a class="btn" href="#" style="position:absolute;left:104px;top:12px;width:72px;height:11px;font-size:3.6px">Travel Protection Options</a>
    <span class="burger" style="left:183px;top:13px"></span>
  </header>

  <div class="hero-photo" style="top:46px;height:95px" role="img" aria-label="Photo of a smiling student traveller holding a map in front of the Eiffel Tower under a blue sky"></div>
  <section class="hero-band" style="top:141px;height:132px;text-align:center">
    <h1 class="hero-title abs" style="left:0;width:100%;top:18px;font-size:18px">Travel Payment<br>Protection</h1>
    <p class="hero-text abs" style="left:14px;width:176px;top:67px;font-size:5.6px;line-height:1.9">Travel Insurance is optional, but unexpected events are always a possibility... and without the Scholar Prime Group Travel Protection, you might lose up to 100% of your trip investment</p>
  </section>

  <section class="abs" style="left:0;top:273px;width:100%;height:302px;background:var(--white);border-bottom:1px solid var(--frame)">
    <h2 class="section-title abs" style="left:0;width:100%;top:24px;font-size:17px;line-height:1.22">Protect your<br>Trip Investment!</h2>
    <p class="intro abs" style="left:12px;width:180px;top:81px;font-size:5.5px;line-height:9.4px">Voyagard Assurance, a leading provider of group travel insurance, offers participants the opportunity to protect their travel investment.This program offers an array of travel protection benefits including 24/7 Worldwide Non-Insurance Assistance Services as well as Trip Cancellation,Trip Interruption, Medical Expense, Baggage and Personal Effects, and more travel insurance coverages such as the Cancel for Any Reason (CFAR) option, if eligible</p>
    <div class="partner" style="left:32px;top:226px;width:140px;height:32px;padding:0 6px;font-size:9px;gap:4px">
      <span class="partner__square" style="width:20px;height:20px"></span>Voyagard Assurance
    </div>
    <p class="cost-line abs" style="left:0;width:100%;top:280px;text-align:center;font-size:6.8px;font-weight:500">To start, please enter your total Trip Cost: <b>$150</b></p>
  </section>

  <article class="plan" style="left:22px;top:594px;width:160px;height:342px">
    <div class="plan__head">None<span class="plan__info">?</span><span class="plan__price">$0</span></div>
    <p class="plan__lead">Potentially lose 100% of your tour cost</p>
    <ul class="plan__list"><li>No Payment Protection</li></ul>
    <div class="plan__foot"><a class="btn plan__select" href="#">Select</a></div>
  </article>

  <a class="feedback-tab" href="#" style="left:13px;top:710px;width:16px;height:131px;font-size:6px"><span>QUESTIONS AND COMMENTS?</span></a>

  <article class="plan plan--featured" style="left:11px;top:948px;width:182px;height:355px">
    <div class="plan__head">Scholar Prime<span class="plan__info">?</span><span class="plan__price">$100</span></div>
    <p class="plan__lead">Protects your trip investment for covered reasons only</p>
    <ul class="plan__list">
      <li>Trip Cancellation coverage provides a 100% refund if you need to cancel for covered reasons</li>
      <li>Includes additional coverages as per below Schedule</li>
      <li class="is-no">Does NOT include Cancel for Any Reason (CFAR)***</li>
      <li class="is-no">No coverage for cancellations due to fear of a pandemic</li>
    </ul>
    <div class="plan__foot"><a class="btn plan__select" href="#">Select</a></div>
  </article>

  <div class="recommended" style="left:0;width:100%;top:1320px">★ Recommended ★</div>

  <article class="plan" style="left:22px;top:1341px;width:160px;height:332px">
    <div class="plan__head" style="font-size:13px;padding-top:10px">Scholar Prime with<br>CFAR<span class="plan__info">?</span><span class="plan__price">$150</span></div>
    <p class="plan__lead">Potentially lose 100% of your tour cost</p>
    <ul class="plan__list" style="font-size:6.6px">
      <li>Trip Cancellation coverage provides a 100% refund if you need to cancel for covered reasons</li>
      <li>Includes additional coverages as per below Schedule</li>
      <li class="is-plus">Includes Cancel for Any Reason (CFAR)***</li>
      <li class="is-plus">Covers cancellation due to fear of a pandemic ***</li>
    </ul>
    <div class="plan__foot"><a class="btn plan__select" href="#">Select</a></div>
  </article>

  <div class="bcol bcol--m" style="left:22px;top:1701px;width:160px">
    <div class="bcol__row bcol__row--head"><span class="bcol__label">BENEFIT</span></div>
    <div class="bcol__row bcol__row--cfar">Cancel for any reason (CFAR)***</div>
    <div class="bcol__row">Trip Cancellation**</div>
    <div class="bcol__row">Trip Interruption**</div>
    <div class="bcol__row">Travel Delay – 6 Hours</div>
    <div class="bcol__row">Missed Connection – 3 Hours</div>
    <div class="bcol__row">Baggage/Personal Effects</div>
    <div class="bcol__row">Baggage Delay – 24 Hours</div>
    <div class="bcol__row bcol__row--tall">Emergency Medical Evacuation, Medical Repatriation &amp; Return of Remains</div>
    <div class="bcol__row">Accident &amp; Sickness Medical Expense</div>
    <div class="bcol__row">Non-Medical Emergency Evacuation</div>
    <div class="bcol__row bcol__row--tall">Non-Insurance Worldwide Emergency Assistance Services</div>
  </div>
  <div class="bcol bcol--m" style="left:22px;top:2090px;width:160px">
    <div class="bcol__row bcol__row--head"></div>
    <div class="bcol__row"><span class="bcol__x">✖</span></div>
    <div class="bcol__row"><span class="bcol__x">✖</span></div>
    <div class="bcol__row"><span class="bcol__x">✖</span></div>
    <div class="bcol__row"><span class="bcol__x">✖</span></div>
    <div class="bcol__row"><span class="bcol__x">✖</span></div>
    <div class="bcol__row"><span class="bcol__x">✖</span></div>
    <div class="bcol__row"><span class="bcol__x">✖</span></div>
    <div class="bcol__row bcol__row--tall"><span class="bcol__x">✖</span></div>
    <div class="bcol__row"><span class="bcol__x">✖</span></div>
    <div class="bcol__row"><span class="bcol__x">✖</span></div>
    <div class="bcol__row bcol__row--tall"><span class="bcol__x">✖</span></div>
  </div>
  <div class="bcol bcol--m" style="left:22px;top:2480px;width:160px">
    <div class="bcol__row bcol__row--head"></div>
    <div class="bcol__row"><span class="bcol__x">✖</span></div>
    <div class="bcol__row">Trip Cost*</div>
    <div class="bcol__row">150% Trip Cost</div>
    <div class="bcol__row">$750 ($150/day)</div>
    <div class="bcol__row">$500</div>
    <div class="bcol__row">$1,500</div>
    <div class="bcol__row">$300</div>
    <div class="bcol__row bcol__row--tall">$100,000</div>
    <div class="bcol__row">$25,000</div>
    <div class="bcol__row">$100,000</div>
    <div class="bcol__row bcol__row--tall">Included</div>
  </div>
  <div class="bcol bcol--m" style="left:22px;top:2870px;width:160px">
    <div class="bcol__row bcol__row--head"></div>
    <div class="bcol__row bcol__row--cfar">Cancel for any reason (CFAR)***: Included</div>
    <div class="bcol__row">Trip Cost*</div>
    <div class="bcol__row">150% of Trip Cost</div>
    <div class="bcol__row">$750 ($150/day)</div>
    <div class="bcol__row">$500</div>
    <div class="bcol__row">$1,500</div>
    <div class="bcol__row">$300</div>
    <div class="bcol__row bcol__row--tall">$100,000</div>
    <div class="bcol__row">$25,000</div>
    <div class="bcol__row">$100,000</div>
    <div class="bcol__row bcol__row--tall">Included</div>
  </div>

  <p class="coverage-note" style="left:9px;top:3280px;width:186px;font-size:8.4px;text-align:center;line-height:1.55">Coverages may vary and not all coverage is available in all jurisdictions. Totals listed below each coverage are the maximum benefit amount payable.</p>
  <div class="footnotes" style="left:9px;top:3366px;width:186px;font-size:5.5px;line-height:11.2px;text-align:center">
    <p><span class="star">*</span> Up to the lesser of the Trip Cost paid or the limit of Coverage for which benefits are requested and the appropriate plan cost has been paid. Maximum limit of $10,000</p>
    <p><span class="star">**</span> For $0 Trip Cost, there is no Trip Cancellation and Trip Interruption is limited to $500 return air only</p>
    <p><span class="star">***</span> CFAR coverage is the lesser of 75% of the nonrefundable trip cost or up to the maximum of $10,000. CFAR is optional and available for purchase on an individual level. Trip cancellation must be 48 hours or more prior to scheduled departure. CFAR must be purchased at the time of plan purchase and with, or before your final payment. CFAR is available if you paid your Travel Supplier for the full cost for all non-refundable trip costs for your trip prior to your cancellation of your trip. For $0 Trip Cost there is no CFAR. <b>This benefit is not available to residents of New York State.</b></p>
  </div>
  <a class="btn" href="#" style="position:absolute;left:15px;top:3678px;width:174px;height:26px;font-size:5.2px;font-weight:500">Click here for limitations and exclusions</a>
  <span class="policy-code" style="left:0;width:100%;text-align:center;top:3714px;font-size:7px">VG-4180</span>

  <footer class="site-footer" style="top:3742px;height:50px;font-size:6.5px;line-height:1.7">© 2020 Halvard Tours.All Rights reserved<br>Privacy Policy &nbsp;|&nbsp; Terms and use</footer>
</main>

</body>
</html>
```